Plumbing Company After Business Card

Business card for a plumbing business that offers a variety of plumbing services including maintenance, domestic and commercial plumbing. My main focus is to offer high quality professional service. A logo on the card would be ideal. Any other questions feel free to email. Cheers

Looking for something modern and upmarket with preferably a matte black background

Business name is Crestline Plumbing and Gas

Industry/Entity Type

Plumbing

Contact Information for Business Card

Crestline Plumbing and Gas
Marcus Thorvale
0472519306
14 Karrabee Drive, Wyndell 3562
crestlineplumbing@mailbay.com.au
ABN 64 915 207 338

Font styles to use
Sans Serif

Colors
1b1b1b
ffffff
3377b5

Requirements
Must have
• Domestic
• Commercial
• Maintenance

```html
<!DOCTYPE html>
<html lang="en">
<head>
<meta charset="utf-8">
<title>Crestline Plumbing and Gas – Business Card</title>
<link href="https://fonts.googleapis.com/css2?family=Anton&family=Open+Sans:wght@400;600;700&display=swap" rel="stylesheet">
<style>
  :root {
    --backdrop: #1f1d1c;
    --brand-blue: #0e406f;
    --accent-blue: #3377b5;
    --ink-black: #1b1b1b;
    --paper-white: #ffffff;
  }
  * { box-sizing: border-box; margin: 0; padding: 0; }
  html, body { width: 1200px; height: 1200px; overflow: hidden; }
  body {
    background: var(--backdrop);
    font-family: "Open Sans", Arial, sans-serif;
    position: relative;
  }
  .card {
    position: absolute;
    left: 220px;
    width: 760px;
    height: 434px;
    border-radius: 26px;
    overflow: hidden;
  }
  /* Front */
  .card-front {
    top: 120px;
    background: var(--brand-blue);
    display: flex;
    align-items: center;
    justify-content: center;
  }
  .front-wordmark {
    color: var(--paper-white);
    font-weight: 700;
    text-align: center;
    text-transform: uppercase;
    line-height: 1.1;
  }
  .front-wordmark .name-main { display: block; font-size: 74px; letter-spacing: 2px; }
  .front-wordmark .name-sub { display: block; font-size: 30px; letter-spacing: 3px; margin-top: 8px; }

  /* Back */
  .card-back {
    top: 640px;
    background: var(--paper-white);
  }
  .back-wordmark {
    position: absolute;
    left: 60px;
    top: 38px;
    color: var(--brand-blue);
    font-weight: 700;
    text-transform: uppercase;
    line-height: 1.1;
  }
  .back-wordmark .name-main { display: block; font-size: 58px; letter-spacing: 2px; }
  .back-wordmark .name-sub { display: block; font-size: 24px; letter-spacing: 3px; margin-top: 4px; }
  .service-band {
    position: absolute;
    left: 0; right: 0;
    top: 186px;
    height: 38px;
    background: var(--ink-black);
    color: var(--paper-white);
    font-weight: 600;
    font-size: 19px;
    letter-spacing: 0.5px;
    display: flex;
    align-items: center;
    justify-content: flex-end;
    padding-right: 44px;
    gap: 10px;
  }
  .service-band .dot {
    width: 8px; height: 8px; border-radius: 50%;
    background: var(--accent-blue);
  }
  .contact-panel {
    position: absolute;
    left: 0; right: 0; bottom: 0;
    top: 224px;
    background: var(--brand-blue);
    color: var(--paper-white);
  }
  .person-name {
    position: absolute;
    left: 56px; top: 12px;
    font-family: "Anton", "Arial Narrow", sans-serif;
    font-size: 36px;
    letter-spacing: 2px;
    color: var(--ink-black);
    text-transform: uppercase;
  }
  .person-role {
    position: absolute;
    left: 58px; top: 64px;
    font-size: 16px;
    font-weight: 600;
    letter-spacing: 1px;
  }
  .contact-list {
    position: absolute;
    left: 58px; top: 112px;
    list-style: none;
    font-size: 17px;
    font-weight: 600;
  }
  .contact-list li { display: flex; align-items: center; gap: 12px; margin-bottom: 10px; }
  .contact-list svg { width: 18px; height: 18px; flex: none; }
  .divider {
    position: absolute;
    left: 432px; top: 104px;
    width: 1.5px; height: 88px;
    background: var(--paper-white);
  }
  .address-block {
    position: absolute;
    left: 456px; top: 116px;
    font-size: 17px;
    font-weight: 600;
    line-height: 1.6;
    text-transform: uppercase;
  }
</style>
</head>
<body>

<section class="card card-front" aria-label="Card front">
  <div class="front-wordmark">
    <span class="name-main">Crestline</span>
    <span class="name-sub">Plumbing and Gas</span>
  </div>
</section>

<section class="card card-back" aria-label="Card back">
  <div class="back-wordmark">
    <span class="name-main">Crestline</span>
    <span class="name-sub">Plumbing and Gas</span>
  </div>

  <div class="service-band">
    <span>DOMESTIC</span><span class="dot"></span>
    <span>COMMERCIAL</span><span class="dot"></span>
    <span>MAINTENANCE</span>
  </div>

  <div class="contact-panel">
    <div class="person-name">Marcus Thorvale</div>
    <div class="person-role">OWNER</div>
    <ul class="contact-list">
      <li>
        <svg viewBox="0 0 18 18" aria-hidden="true">
          <rect x="0" y="0" width="18" height="18" rx="3" fill="#1b1b1b"/>
          <path d="M5 3.5c-1 .5-1.5 1.5-1 3 1 3 3.5 5.5 6.5 6.5 1.5.5 2.5 0 3-1l-2-2-1.5 1c-1.5-.7-2.8-2-3.5-3.5l1-1.5z" fill="#fff"/>
        </svg>
        <span>0472519306</span>
      </li>
      <li>
        <svg viewBox="0 0 18 18" aria-hidden="true">
          <rect x="0" y="0" width="18" height="18" rx="3" fill="#1b1b1b"/>
          <rect x="3" y="5" width="12" height="8" fill="none" stroke="#fff" stroke-width="1.4"/>
          <path d="M3 5l6 5 6-5" fill="none" stroke="#fff" stroke-width="1.4"/>
        </svg>
        <span>crestlineplumbing@mailbay.com.au</span>
      </li>
    </ul>
    <div class="divider"></div>
    <div class="address-block">
      14 Karrabee Drive, Wyndell 3562<br>
      ABN 64 915 207 338
    </div>
  </div>
</section>

</body>
</html>
```